Kelvara Drift Marine Voyages LLC Web Design Project

We are KDMV "Kelvara Drift Marine Voyages LLC" located in Juneau Alaska. We are a multi-faceted company that offers Research, Consultation, Retail, Renewable Energy Education in maritime environments, and eco tourism with zero carbon emissions off our all electric 50 foot Catamaran, EV Kelvara Drift.
We will sell Voltarine electric marine motors for recreational and commercial use and facilitate the transition from fossil fuel to electric and show the fiscal benefits to our customers.
We have great Whale watching, Brackwell Icefield sightseeing and commercial tourism opportunities fed by the cruise ship industry. We have Commercial Fishing, and environmentally sensitive audience that would like to reduce dependency on fossil fuel and support a clean environment. We want to educate our customers about Wind/Solar and Hydro renewable energy. Juneau has it's own independent power grid that is all hydroelectricity. The tourism industry brings about 1.2M to Juneau every summer.
Target Market(s)
Whale Watch and sightseeing, tourism, photographers, STEM education, environmentally sensitive, innovative and curious. Commercial Fishing Industry and Recreational and commercial boaters form Kayaks to Longliner vessels.
Industry/Entity Type
Tourism
Requirements
Must have
- Environmentally Friendly with zero carbon emissions, intelligent and conservative but artistic. KDMV final Logo is currently under construction.
Nice to have
- Sub Titles for Marine Research, Pictures, Renewable energy education, Retail and transition consultation with links to Voltarine.example , booking tours on Kelvara Drift

```html
<!DOCTYPE html>
<html lang="en">
<head>
<meta charset="utf-8">
<title>Kelvara Drift Marine Voyages LLC</title>
<link rel="stylesheet" href="https://fonts.googleapis.com/css2?family=Raleway:wght@400;500;600&family=Open+Sans:wght@400;600&display=swap">
<style>
:root{
  --navy:#14213a;
  --navy-deep:#101c30;
  --navy-bar:#253349;
  --white:#ffffff;
  --ink:#222831;
  --muted:#4a4f57;
  --card:#eeeeee;
  --accent-blue:#2a62b4;
  --input:#8a909a;
  --footer-text:#e6e9ee;
}
*{margin:0;padding:0;box-sizing:border-box}
html,body{width:1200px;height:2452px;overflow:hidden;background:var(--white)}
body{position:relative;font-family:"Raleway",sans-serif;color:var(--ink)}
.abs{position:absolute}

/* Header */
.site-header{left:0;top:0;width:1200px;height:118px;background:var(--white)}
.brand{left:65px;top:34px;display:flex;align-items:center;gap:12px}
.brand-dot{width:40px;height:40px;border-radius:50%;background:var(--navy)}
.brand-name{font-family:"Raleway",sans-serif;font-weight:600;font-size:24px;color:var(--navy)}
.phone{right:65px;top:20px;display:flex;align-items:center;gap:8px;font-size:16px;color:#444}
.phone-icon{width:22px;height:22px;border-radius:50%;background:#444;display:flex;align-items:center;justify-content:center}
.main-nav{right:60px;top:62px;display:flex;gap:0}
.main-nav a{display:block;height:33px;line-height:33px;padding:0 17px;font-size:14px;color:var(--ink);text-decoration:none}
.main-nav a.active{background:var(--navy);color:var(--white)}

/* Hero */
.hero{left:0;top:118px;width:1200px;height:703px;background:linear-gradient(180deg,#b3c9df 0%,#a9c0d8 55%,#6d8fae 58%,#4e7598 80%,#7d9ab5 100%)}
.hero-band{left:0;top:821px;width:1200px;height:108px;background:var(--navy);color:var(--white);font-size:31px;font-weight:400;text-align:center;line-height:108px}

/* About */
.about-title{left:0;top:970px;width:1200px;text-align:center;font-size:36px;font-weight:400;color:var(--ink)}
.about-text{left:200px;top:1040px;width:800px;text-align:center;font-size:16.5px;line-height:21px;color:var(--muted)}

/* Service cards */
.card{width:342px;height:356px;background:var(--card)}
.card-photo{width:342px;height:149px}
.card-title{position:absolute;left:24px;top:176px;width:300px;font-size:24px;line-height:30px;font-weight:400;color:var(--ink)}
.card-text{position:absolute;left:24px;width:290px;font-family:"Open Sans",sans-serif;font-size:12.5px;line-height:18px;color:var(--muted)}
.card-btn{position:absolute;right:0;bottom:0;width:85px;height:23px;background:var(--navy);color:var(--white);font-family:"Open Sans",sans-serif;font-size:12px;text-align:center;line-height:23px}

/* Testimonials */
.reviews-title{left:0;top:1924px;width:1200px;text-align:center;font-size:25px;color:var(--ink);display:flex;justify-content:center;align-items:center;gap:40px}
.review{height:106px;background:var(--navy);display:flex}
.review-photo{width:160px;height:106px}
.review-body{padding:18px 0 0 30px;color:var(--white);font-size:12px;line-height:20px;width:300px}
.review-body strong{font-weight:600}

/* Footer */
.site-footer{left:0;top:2147px;width:1200px;height:240px;background:var(--navy)}
.footer-bar{left:0;top:2387px;width:1200px;height:65px;background:var(--navy-bar);color:#9aa3b0;font-size:11px}
.footer-brand{left:65px;top:2178px;display:flex;align-items:center;gap:10px}
.footer-brand .brand-dot{background:var(--white);width:34px;height:34px}
.footer-brand .brand-name{color:var(--white);font-size:21px}
.address{left:65px;top:2261px;color:var(--footer-text);font-size:11px;line-height:15px}
.social{left:65px;top:2325px;display:flex;gap:8px}
.social span{width:26px;height:26px;border-radius:50%;background:var(--accent-blue)}
.footer-col h4{font-size:12px;font-weight:600;color:var(--white);margin-bottom:17px}
.footer-col li{list-style:none;font-size:12px;line-height:21px;color:var(--footer-text)}
.email{left:858px;top:2214px;width:278px;height:33px;background:var(--input);color:#dde;font-size:11px;padding:0 10px;line-height:33px}
.subscribe{left:858px;top:2256px;width:120px;height:33px;background:var(--accent-blue);color:var(--white);font-size:16px;text-align:center;line-height:33px}
</style>
</head>
<body>

<header class="abs site-header">
  <div class="abs brand"><span class="brand-dot"></span><span class="brand-name">Kelvara Drift</span></div>
  <div class="abs phone">
    <span class="phone-icon"><svg width="12" height="12" viewBox="0 0 24 24"><path fill="#fff" d="M6.6 10.8a15.1 15.1 0 0 0 6.6 6.6l2.2-2.2c.3-.3.7-.4 1-.2 1.1.4 2.3.6 3.6.6.6 0 1 .4 1 1V20c0 .6-.4 1-1 1C10.6 21 3 13.4 3 4c0-.6.4-1 1-1h3.5c.6 0 1 .4 1 1 0 1.3.2 2.5.6 3.6.1.3 0 .7-.2 1z"/></svg></span>
    +80045127
  </div>
  <nav class="abs main-nav">
    <a class="active" href="#">Home</a><a href="#">Our Mission</a><a href="#">Our Services</a><a href="#">About Us</a><a href="#">Contact Us</a>
  </nav>
</header>

<div class="abs hero" role="img" aria-label="Humpback whale tail rising above grey-blue sea under a pale sky"></div>
<div class="abs hero-band">Lorem Ipsum is simply dummy text of the printing and typesetting industry.</div>

<h1 class="abs about-title">About Kelvara Drift Marine Voyages LLC</h1>
<p class="abs about-text">Lorem Ipsum is simply dummy text of the printing and typesetting industry. Lorem Ipsum has been the industry's standard dummy text ever since the 1500s, when an unknown printer took a galley of type and scrambled it to make a type specimen book.</p>

<!-- Row 1 -->
<article class="abs card" style="left:62px;top:1149px">
  <div class="card-photo" role="img" aria-label="Lake shore with a bench and green hills" style="background:linear-gradient(180deg,#9fb2c4 0%,#6f8a6a 40%,#8fa1a8 70%,#5d7a4a 100%)"></div>
  <h3 class="card-title">Echo Tourism</h3>
  <p class="card-text" style="top:210px">Lorem Ipsum is simply dummy text of the printing and typesetting industry. Lorem Ipsum has been the industry's standard dummy text ever since the 1500s, when an unknown printer took a galley of type and scrambled it to make a</p>
  <span class="card-btn">Read More</span>
</article>
<article class="abs card" style="left:428px;top:1149px">
  <div class="card-photo" role="img" aria-label="Windmill silhouette against an orange sunset" style="background:linear-gradient(180deg,#f2a21a 0%,#e07a10 55%,#3b2a1a 100%)"></div>
  <h3 class="card-title">Renewable Energy Education</h3>
  <p class="card-text" style="top:240px">Lorem Ipsum is simply dummy text of the printing and typesetting industry. Lorem Ipsum has been the industry's standard dummy text ever since the 1500s, type specimen book.</p>
  <span class="card-btn">Read More</span>
</article>
<article class="abs card" style="left:793px;top:1149px">
  <div class="card-photo" role="img" aria-label="Fresh fish laid out at a market" style="background:linear-gradient(90deg,#9aa6b0 0%,#c9b9b4 30%,#d8504a 60%,#e06a5a 100%)"></div>
  <h3 class="card-title">Commercial Fishing</h3>
  <p class="card-text" style="top:210px">Lorem Ipsum is simply dummy text of the printing and typesetting industry. Lorem Ipsum has been the industry's standard dummy text ever since the 1500s, when an unknown printer took a galley of type and scrambled it to make a</p>
  <span class="card-btn">Read More</span>
</article>

<!-- Row 2 -->
<article class="abs card" style="left:62px;top:1530px">
  <div class="card-photo" role="img" aria-label="Snowy mountains reflected in a glacier lake" style="background:linear-gradient(180deg,#3d7fc4 0%,#a9c6e0 40%,#e9eef2 52%,#7fa7c8 75%,#5a8ab8 100%)"></div>
  <h3 class="card-title">Brackwell Icefield Sightseeing</h3>
  <p class="card-text" style="top:240px">Lorem Ipsum is simply dummy text of the printing and typesetting industry. Lorem Ipsum has been the industry's standard dummy text ever since the 1500s, type specimen book.</p>
  <span class="card-btn">Read More</span>
</article>
<article class="abs card" style="left:428px;top:1530px">
  <div class="card-photo" role="img" aria-label="Cruise ship docked in a harbour below green hills" style="background:linear-gradient(180deg,#5aa0d8 0%,#4e7a4a 40%,#e8eef2 65%,#2a6ab0 100%)"></div>
  <h3 class="card-title">Commercial Tourism Opportunities</h3>
  <p class="card-text" style="top:240px">Lorem Ipsum is simply dummy text of the printing and typesetting industry. Lorem Ipsum has been the industry's standard dummy text ever since the 1500s, type specimen book.</p>
  <span class="card-btn">Read More</span>
</article>
<article class="abs card" style="left:793px;top:1530px">
  <div class="card-photo" role="img" aria-label="Hydroelectric dam wall under a blue sky" style="background:linear-gradient(160deg,#3e6fa8 0%,#8fb0d2 45%,#dfe6ee 75%,#b9c7d6 100%)"></div>
  <h3 class="card-title">Independent Power Grid</h3>
  <p class="card-text" style="top:210px">Lorem Ipsum is simply dummy text of the printing and typesetting industry. Lorem Ipsum has been the industry's standard dummy text ever since the 1500s, when an unknown printer took a galley of type and scrambled it to make a</p>
  <span class="card-btn">Read More</span>
</article>

<!-- Testimonials -->
<h2 class="abs reviews-title">
  <svg width="14" height="24" viewBox="0 0 14 24"><path d="M12 2 2 12l10 10" fill="none" stroke="#c8c8c8" stroke-width="2"/></svg>
  <span>Our Happy Customers</span>
  <svg width="14" height="24" viewBox="0 0 14 24"><path d="m2 2 10 10L2 22" fill="none" stroke="#222" stroke-width="2"/></svg>
</h2>
<div class="abs review" style="left:62px;top:1987px;width:513px">
  <div class="review-photo" role="img" aria-label="Portrait of a customer" style="background:linear-gradient(135deg,#6b4a32,#b58a6a)"></div>
  <div class="review-body">Lorem ipsum dolor sit amet, consectetur adipiscing elit. Integer nec odio. Praesent libero. nec odio. Praesent libero.<br><strong>Arlo Pennick</strong></div>
</div>
<div class="abs review" style="left:615px;top:1987px;width:521px">
  <div class="review-photo" role="img" aria-label="Portrait of a customer" style="background:linear-gradient(135deg,#3a2a22,#a57c62)"></div>
  <div class="review-body">Lorem ipsum dolor sit amet, consectetur adipiscing elit. Integer nec odio. Praesent libero. nec odio. Praesent libero.<br><strong>Devin Marsh</strong></div>
</div>

<!-- Footer -->
<footer class="abs site-footer"></footer>
<div class="abs footer-brand"><span class="brand-dot"></span><span class="brand-name">Kelvara Drift</span></div>
<p class="abs address">Suite 4, 27 Harbor Lane Wharfside<br>99801 Juneau, Alaska<br>Tel: +1 907 555 0140, Fax: +1 907 555 0188</p>
<div class="abs social"><span></span><span></span><span></span><span></span></div>

<div class="abs footer-col" style="left:422px;top:2190px">
  <h4>Who We Are</h4>
  <ul><li>Home</li><li>Our Mission</li><li>About Us</li><li>Press Release</li><li>Contact Us</li></ul>
</div>
<div class="abs footer-col" style="left:574px;top:2190px">
  <h4>What We Do</h4>
  <ul><li>Echo Tourism</li><li>Renewable Enery Education</li><li>Commercial Fishing</li><li>Brackwell Icefield Sightseeing</li><li>Commercial Tourism Opportunities</li><li>Independent Power Grid</li></ul>
</div>
<div class="abs footer-col" style="left:858px;top:2190px"><h4>Subscribe Email Newsletter</h4></div>
<div class="abs email">Email</div>
<div class="abs subscribe">Subscribe</div>

<div class="abs footer-bar">
  <span class="abs" style="left:63px;top:26px">Copyright © 2014 Kelvara Drift Marine Voyages LLC</span>
  <span class="abs" style="left:982px;top:26px">Sitemap</span>
  <span class="abs" style="left:1052px;top:26px">Privacy Policy</span>
</div>

</body>
</html>
```